Premium Gold Vodka Label Design

English ------------------- We need a label for a Vodka Bottle. Its a sparkling premium vodka with gold inside. The design should look premium. We tried it on our selves but it looks horrible. Therefore we need your help. The current name is lumora K, but we are open for any better suggestion. We attached the selfmade design. The label will be printed on the bottle. We have other design jobs for you (logo, other sorts)! English ------------------------ We need a label for a vodka bottle. This is a premium vodka which is offset with gold. The design should look like this. We have tried so far and failed. That is why we need your support. The name is so far lumora K. If you have better suggestions we would be pleased about other suggestions / ideas. In the appendix the failed design is stored. The label is to be applied by screen printing. In the case of good work follow-up projects are guaranteed (logo, other varieties, etc)!
Updates

Project Deadline Extended
Reason: We need more time for the decision.

Target Market(s)

USA

Colors

Designer to choose colors to be used in the design.

Requirements
Must have
• English ------------------------ The needed text is on our selfmade label that is attached. English ------------------------ The required texts are stored in the attached design.
Nice to have
• English ------------------------ Transparent places are allowed because we want to print the label on the bottom. English ------------------------ As the label is applied by screen printing, transparent areas are also possible.

```html
<!DOCTYPE html>
<html lang="en">
<head>
<meta charset="utf-8">
<title>lumora K Vodka – Label Artwork</title>
<link rel="stylesheet" href="https://fonts.googleapis.com/css2?family=Roboto:wght@300;400;500;700&display=swap">
<style>
  :root {
    --blue: #1a6fd0;
    --blue-deep: #0f5bb8;
    --grey-text: #6e6e6e;
    --panel: #ffffff;
    --panel-edge: #e2e4e8;
    --page: #eeeeef;
    --splash-light: #e6f1fb;
    --splash-mid: #a9cdee;
  }
  html, body {
    margin: 0;
    padding: 0;
    width: 1200px;
    height: 1200px;
    overflow: hidden;
  }
  body {
    background: linear-gradient(#e4e4e5, #f7f7f7 60%, #f0f0f0);
    font-family: "Roboto", sans-serif;
    position: relative;
  }
  .label-sheet {
    position: absolute;
    top: 110px;
    width: 400px;
    height: 900px;
    background: var(--panel);
    border: 1px solid var(--panel-edge);
    box-sizing: border-box;
  }
  .label-sheet--front { left: 170px; }
  .label-sheet--back  { left: 630px; }

  .caption {
    position: absolute;
    top: 1040px;
    width: 400px;
    text-align: center;
    font-size: 28px;
    font-weight: 300;
    color: var(--grey-text);
  }
  .caption--front { left: 170px; }
  .caption--back  { left: 630px; }

  /* Front */
  .brand-name {
    position: absolute;
    top: 300px;
    left: 0;
    width: 100%;
    text-align: center;
    font-size: 60px;
    font-weight: 500;
    color: var(--blue);
    margin: 0;
  }
  .splash-art {
    position: absolute;
    top: 390px;
    left: 60px;
    width: 280px;
    height: 190px;
    border-radius: 50% 50% 45% 55% / 55% 45% 55% 45%;
    background: radial-gradient(ellipse at 55% 60%, var(--splash-mid), var(--splash-light) 70%, transparent 72%);
  }
  .product-block {
    position: absolute;
    top: 600px;
    left: 70px;
    width: 260px;
    text-align: center;
  }
  .product-karat, .product-descriptor {
    font-size: 20px;
    font-weight: 300;
    color: var(--grey-text);
    line-height: 1.1;
  }
  .product-descriptor {
    border-bottom: 1px solid var(--blue);
    padding-bottom: 6px;
  }
  .product-type {
    font-size: 66px;
    font-weight: 500;
    color: var(--blue);
    letter-spacing: 1px;
    line-height: 1;
    padding: 8px 0 6px;
    border-bottom: 1px solid var(--blue);
  }
  .filtration {
    margin-top: 6px;
    font-size: 19px;
    font-weight: 300;
    color: var(--grey-text);
    display: flex;
    justify-content: space-between;
    align-items: center;
  }
  .filtration-count {
    font-size: 36px;
    font-weight: 700;
    color: var(--blue);
    line-height: 1;
  }
  .legal-info {
    position: absolute;
    top: 820px;
    right: 40px;
    text-align: right;
    font-size: 11px;
    font-weight: 300;
    color: var(--grey-text);
    line-height: 1.3;
  }

  /* Back */
  .back-copy {
    position: absolute;
    top: 600px;
    left: 40px;
    width: 320px;
  }
  .back-title {
    margin: 0;
    font-size: 30px;
    font-weight: 300;
    color: var(--grey-text);
    border-bottom: 1px solid var(--blue);
    padding-bottom: 2px;
  }
  .back-text {
    margin: 8px 0 0;
    font-size: 14px;
    font-weight: 300;
    color: var(--blue-deep);
    line-height: 1.3;
    text-align: justify;
    padding-bottom: 6px;
    border-bottom: 1px solid var(--blue);
  }
</style>
</head>
<body>
  <section class="label-sheet label-sheet--front">
    <h1 class="brand-name">lumora K</h1>
    <div class="splash-art" role="img" aria-label="Splash of clear water in light blue tones"></div>
    <div class="product-block">
      <div class="product-karat">24Kt</div>
      <div class="product-descriptor">Premium Gold Sparkling</div>
      <div class="product-type">VODKA</div>
      <div class="filtration">
        <span>DISTILLED</span>
        <span class="filtration-count">8</span>
        <span>FILTERED</span>
      </div>
    </div>
    <div class="legal-info">
      Made in GERMANY<br>
      40%Alc Vol&nbsp;&nbsp;80Proof&nbsp;&nbsp;200ml
    </div>
  </section>

  <section class="label-sheet label-sheet--back">
    <div class="back-copy">
      <h2 class="back-title">VODKA</h2>
      <p class="back-text">is a distilled beverage composed primarily of water and ethanol, sometimes with traces of impurities and flavorings. Traditionally, vodka is made by the distillation of cereal grains or potatoes that have been fermented, though some modern brands use other substances, such as fruits or sugar. (reference)</p>
    </div>
  </section>

  <div class="caption caption--front">front</div>
  <div class="caption caption--back">back</div>
</body>
</html>
```